Rocket business card

Modern business card design, use of color is good with clean space too.

Things to include on card:

Quote: I add fuel to your optometry practice

- Eyewear Sales
- Admin Duties
- Revenue Collection
- Leadership
- Tech Adoption
- COGS Reduction
- Product Sourcing
-Medical Growth

Dalton Vesk, CEO
Lume Vantor
Text Me! 847-302-6194
dalton@lumevantor.net

```html
<!DOCTYPE html>
<html lang="en">
<head>
<meta charset="utf-8">
<title>Lume Vantor – Business Card</title>
<link href="https://fonts.googleapis.com/css2?family=Lato:wght@400;700;900&display=swap" rel="stylesheet">
<style>
  :root {
    --bg: #2e2e2e;
    --white: #ffffff;
    --ink: #1a1a1a;
    --orange: #f0821e;
    --orange-deep: #e8571f;
    --red: #e03a2f;
    --amber: #f6a01e;
    --disc-grey: #efefef;
  }
  * { box-sizing: border-box; margin: 0; padding: 0; }
  html, body { width: 1200px; height: 866px; overflow: hidden; }
  body {
    background: var(--bg);
    font-family: "Lato", sans-serif;
    display: flex;
    flex-direction: column;
    align-items: center;
    justify-content: center;
    gap: 34px;
  }
  .card {
    position: relative;
    width: 680px;
    height: 388px;
    overflow: hidden;
    box-shadow: 0 10px 24px rgba(0,0,0,.45);
  }
  /* front */
  .card--front { background: var(--white); border-bottom: 6px solid var(--orange); }
  .card--front .disc {
    position: absolute; left: 170px; top: -40px;
    width: 400px; height: 400px; border-radius: 50%;
    background: var(--disc-grey);
  }
  .brand {
    position: absolute; display: flex; align-items: center; gap: 16px;
  }
  .card--front .brand { left: 150px; top: 120px; }
  .brand__dot {
    width: 58px; height: 58px; border-radius: 50%;
    background: var(--orange-deep);
  }
  .brand__name {
    font-weight: 400; font-size: 54px; letter-spacing: 3px;
    text-transform: uppercase; color: var(--ink); line-height: 1;
  }
  .person {
    position: absolute; left: 60px; top: 250px;
    font-size: 22px; color: var(--ink);
  }
  .person__name { color: var(--orange-deep); font-weight: 900; letter-spacing: 1px; text-transform: uppercase; }
  .contact {
    position: absolute; left: 60px; top: 300px;
    font-size: 21px; color: var(--ink);
  }
  .contact__label { color: var(--orange); }
  /* back */
  .card--back {
    background: linear-gradient(120deg, var(--amber) 0%, var(--orange) 45%, var(--red) 100%);
  }
  .card--back .disc {
    position: absolute; left: 260px; top: -50px;
    width: 420px; height: 420px; border-radius: 50%;
    background: rgba(255,200,60,.28);
  }
  .card--back .brand { left: 90px; top: 90px; }
  .card--back .brand__name { color: var(--white); font-size: 60px; }
  .tagline {
    position: absolute; left: 90px; top: 172px;
    color: var(--white); font-weight: 900; font-size: 19px;
    text-transform: uppercase; letter-spacing: .5px;
  }
  .services {
    position: absolute; left: 90px; top: 220px;
    color: var(--white); font-size: 20px; line-height: 1.45; list-style: none;
  }
</style>
</head>
<body>
  <section class="card card--front">
    <div class="disc"></div>
    <div class="brand">
      <span class="brand__name">Lume Vantor</span>
    </div>
    <p class="person"><span class="person__name">Dalton Vesk</span>, CEO</p>
    <p class="contact"><span class="contact__label">Text Me!</span> 847-302-6194 <span class="contact__label">| E:</span> dalton@lumevantor.net</p>
  </section>

  <section class="card card--back">
    <div class="disc"></div>
    <div class="brand">
      <span class="brand__name">Lume Vantor</span>
    </div>
    <p class="tagline">I add fuel to your optometry practice</p>
    <ul class="services">
      <li>Eyewear Sales • Admin Duties • Revenue Collection</li>
      <li>Leadership • Tech Adoption • COGS Reduction</li>
      <li>Product Sourcing • Medical Growth</li>
    </ul>
  </section>
</body>
</html>
```